AI Layout work for Business Cards, Letterhead and Compliment Slip for Award-winning UK Property Deve

No actual logo or corporate identity design work needed here but some skill required to create layouts for business card, letterhead and compliment slip for this award-winning company.
I can provide AI files featuring the company logo and an initial layout of the business card, (6 versions featuring the same design but for different personnel), along with some initial instructions (with possibly more to follow from the client). The finished layouts for each item need to be print-ready in AI format - 8 in all (6 for each business card plus 1 for letterhead and 1 for compliment slip).
I've given this project a 5-day duration but there may be some flexibility built into that depending on client feedback. Hopefully that won't be a problem.
UPDATE:
The client has been very prescriptive about the layout and design of these. To that end, please find 3 additional pdfs that explain what's required.
1.
All BUSINESS CARDS need to be laid out as per the attached AI file (but see latest pdf to check which layout - there are 2 in the original AI file). Use the details in the RUNE-contact-details.pdf to create 6 individual AI files, one for each card.
2.
Create 2 additional AI files, one each for the LETTERHEAD and the COMPLIMENT SLIP based on the latest mock-up that I've provided (letterhead-layout-final.pdf)
In all, I need EIGHT individual AI files, 6 for each business card, 1 for the letterhead and 1 for the compliment slip. I'd like to get this done as soon as possible now please.
Target Market(s)
Purchasers of upmarket luxury properties - see here: http://www.runeestates.co.uk
Industry/Entity Type
Business
Requirements
Must have
- Layouts need to be cool, understated and uncluttered.
Nice to have
- Please keep it simple! The actual logo background colour is likely to change (awaiting confirmation from client) but accompanying text detail and font (Deja Vu Sans Condensed) can remain as seen in the files below - for the time being at least! That having been said, I'm open to suggestions.
Should not have
- Nothing extreme or ostentatious please.

```html
<!DOCTYPE html>
<html lang="en">
<head>
<meta charset="utf-8">
<title>RUNE Estates – Stationery Layouts</title>
<link rel="stylesheet" href="https://fonts.googleapis.com/css2?family=PT+Sans:wght@400;700&family=PT+Sans+Narrow:wght@400;700&family=Roboto+Condensed:wght@700&display=swap">
<style>
  :root {
    --navy: #0b0f5c;
    --navy-soft: #2a3585;
    --white: #ffffff;
    --ink: #111111;
    --grey-line: #bfc3cc;
    --cyan: #22eef0;
    --sand: #b49a62;
    --pink: #f4e3ef;
    --peach: #f0cfa8;
    --silver: #c9cdcf;
    --silver-dark: #8e9496;
    --sky: #7fdcf2;
    --blue-card: #3f6ff2;
    --tag-yellow: #f7e27a;
    --mint: #9af0c8;
    --violet: #7a3fc9;
  }
  * { box-sizing: border-box; margin: 0; padding: 0; }
  html, body { width: 1047px; height: 1200px; overflow: hidden; background: var(--white); }
  body { position: relative; font-family: "PT Sans Narrow", "Arial Narrow", sans-serif; color: var(--ink); }

  .section-label { position: absolute; font-family: "Roboto Condensed", sans-serif; font-weight: 700; font-size: 12px; color: var(--ink); }

  .card { position: absolute; width: 352px; height: 179px; overflow: hidden; border: 1px solid #333; }
  .card > * { position: absolute; }
  .artwork { display: block; }

  .brand-box { background: var(--navy); color: var(--white); display: flex; align-items: center; justify-content: center; gap: 7px; }
  .brand-name { font-family: "PT Sans", sans-serif; font-weight: 400; font-size: 22px; color: var(--white); letter-spacing: 1px; }
  .brand-mark { width: 8px; height: 8px; background: var(--white); }

  .person { font-family: "PT Sans", sans-serif; line-height: 1; text-align: center; }
  .person-name { font-size: 27px; }
  .person-role { font-size: 14px; margin-top: 2px; }
  .person.light { color: var(--white); text-shadow: 0 1px 2px rgba(0,0,0,.45); }
  .person.dark { color: var(--navy); }

  .contact { list-style: none; font-size: 10px; font-weight: 700; line-height: 17px; color: var(--navy); }
  .contact li { display: flex; align-items: center; gap: 5px; }
  .icon { width: 11px; height: 11px; flex: none; }
  .address { list-style: none; font-size: 10px; font-weight: 700; line-height: 14px; color: var(--navy); }
  .address.right { text-align: right; }
  .address.right li { display: flex; justify-content: flex-end; align-items: center; gap: 4px; }
  .dot { width: 7px; height: 7px; border-radius: 50%; background: #3d6fe0; flex: none; }

  /* Card 1 */
  .card-sky { background: linear-gradient(180deg, var(--cyan) 0%, #4fe3df 55%, var(--sand) 100%); }
  .card-sky .address-strip { left: 0; top: 0; width: 100%; height: 20px; background: var(--white); display: flex; align-items: center; justify-content: space-around; font-size: 10px; font-weight: 700; color: var(--ink); }
  .card-sky .address-strip span + span { border-left: 1px solid #333; padding-left: 8px; }

  /* Card 2 */
  .card-blush { background: var(--pink); }
  /* Card 3 */
  .card-silver { background: linear-gradient(135deg, #e6e8e8 0%, var(--silver) 50%, var(--silver-dark) 100%); }
  /* Card 4 */
  .card-panel { background: var(--white); }
  /* Card 5 */
  .card-aqua { background: linear-gradient(135deg, #c8f3fb 0%, var(--sky) 60%, #4bc3ea 100%); }
  /* Card 6 */
  .card-mist { background: linear-gradient(90deg, #dfe3e3 0%, #f7f8f8 50%, #cfd4d4 100%); }

  /* Letterhead */
  .letterhead { position: absolute; left: 72px; top: 665px; width: 765px; height: 110px; background: var(--navy); color: var(--white); }
  .letterhead > * { position: absolute; }
  .letterhead .address-line { right: 0; top: 5px; height: 13px; padding: 0 14px 0 120px; font-size: 9.5px; font-weight: 700; background: linear-gradient(90deg, rgba(255,255,255,0) 0%, rgba(255,255,255,.35) 100%); line-height: 13px; }
  .bullet-sep { margin: 0 5px; }
  .letterhead .brand { left: 22px; top: 30px; }
  .sign-block { text-align: right; font-family: "PT Sans", sans-serif; }
  .sign-block .name { font-size: 14px; margin-bottom: 5px; }
  .sign-block .lines { font-size: 9.5px; line-height: 14px; font-weight: 700; font-family: "PT Sans Narrow", sans-serif; }
  .letterhead .sign-block { right: 16px; top: 38px; }

  /* Compliment slip */
  .slip { position: absolute; left: 97px; top: 831px; width: 725px; height: 362px; border: 1px solid var(--grey-line); overflow: hidden; background: var(--white); }
  .slip > * { position: absolute; }
  .slip-header { left: 0; top: 0; width: 100%; height: 96px; background: var(--navy); display: flex; align-items: center; justify-content: center; }
  .slip-rule { left: 0; top: 102px; width: 100%; height: 8px; background: var(--navy); }
  .slip-curve { right: 0; bottom: 0; }
  .slip .sign-block { right: 14px; bottom: 36px; color: var(--white); }
  .slip-footer { left: 0; bottom: 0; width: 100%; height: 24px; background: linear-gradient(90deg, #ffffff 0%, #5b63a3 18%, var(--navy) 35%, var(--navy) 65%, #5b63a3 82%, #ffffff 100%); color: var(--white); font-size: 9.5px; font-weight: 700; display: flex; align-items: center; justify-content: center; }
</style>
</head>
<body>

<h2 class="section-label" style="left:105px; top:16px;">Business Card</h2>

<!-- Card 1 -->
<section class="card card-sky" style="left:105px; top:35px;">
  <div class="address-strip"><span>RUNE Exclusive Estates</span><span>Elm Court House</span><span>Elm Court Lane</span><span>Amersham Vale</span><span>HP9 2QX</span></div>
  <div role="img" aria-label="Illustration of a house roof" style="left:170px; top:28px; width:170px; height:85px; background:linear-gradient(180deg, rgba(255,255,255,.55), rgba(255,255,255,0)); border-radius:4px;"></div>
  <ul class="contact" style="left:6px; top:38px;">
    <li><svg class="icon" viewBox="0 0 12 12"><path d="M2 1h3l1 3-2 1a6 6 0 0 0 3 3l1-2 3 1v3a1 1 0 0 1-1 1A10 10 0 0 1 1 2a1 1 0 0 1 1-1z" fill="#d89a1a"/></svg>t: +44 (0)1632 960415</li>
    <li><svg class="icon" viewBox="0 0 12 12"><rect x="1" y="3" width="10" height="7" fill="#e8b830"/><path d="M1 3l5 4 5-4" stroke="#fff" fill="none"/></svg>e: enquiries@runeestates.co.uk</li>
    <li><svg class="icon" viewBox="0 0 12 12"><circle cx="6" cy="6" r="5" fill="#2f6fd0"/><path d="M1 6h10M6 1v10" stroke="#fff" stroke-width=".8"/></svg>w: runeestates.co.uk</li>
  </ul>
  <div class="brand-box" style="left:9px; top:101px; width:112px; height:67px;"><span class="brand-mark"></span><span class="brand-name">RUNE</span></div>
  <div class="person light" style="left:135px; top:122px; width:200px;"><div class="person-name">Daniel Hart</div><div class="person-role">Director</div></div>
</section>

<!-- Card 2 -->
<section class="card card-blush" style="left:469px; top:35px;">
  <div style="left:64px; top:0; width:22px; height:100%; background:var(--navy-soft);"></div>
  <div role="img" aria-label="Illustration of an open hand" style="left:150px; top:0; width:150px; height:110px; background:radial-gradient(ellipse at 55% 40%, var(--peach) 0%, rgba(240,207,168,0) 70%);"></div>
  <p style="left:105px; top:5px; font-size:10px; font-weight:700; color:var(--navy);">RUNE Exclusive Estates</p>
  <ul class="address" style="left:246px; top:5px; color:var(--ink);"><li>Elm Court House</li><li>Elm Court Lane</li><li>Amersham Vale</li><li>HP9 2QX</li></ul>
  <div class="brand-box" style="left:22px; top:47px; width:112px; height:65px;"><span class="brand-mark"></span><span class="brand-name">RUNE</span></div>
  <div class="person dark" style="left:150px; top:68px; width:190px;"><div class="person-name">Daniel Hart</div><div class="person-role">Director</div></div>
  <ul class="contact" style="left:195px; top:120px; line-height:15px;"><li>t: +44 (0)1632 960415</li><li>e: enquiries@runeestates.co.uk</li><li>w: runeestates.co.uk</li></ul>
</section>

<!-- Card 3 -->
<section class="card card-silver" style="left:105px; top:225px;">
  <div role="img" aria-label="Line drawing of a period building" style="left:90px; top:15px; width:150px; height:110px; background:linear-gradient(180deg, rgba(255,255,255,.45), rgba(255,255,255,.1)); border-radius:3px;"></div>
  <ul class="address right" style="left:0; top:6px; width:110px; color:var(--ink);"><li>RUNE Exclusive Estates<span class="dot"></span></li><li>Elm Court House<span class="dot"></span></li><li>Elm Court Lane<span class="dot"></span></li><li>Amersham Vale<span class="dot"></span></li><li>HP9 2QX<span class="dot"></span></li></ul>
  <div class="brand-box" style="left:222px; top:36px; width:122px; height:74px;"><span class="brand-mark"></span><span class="brand-name">RUNE</span></div>
  <div class="person light" style="left:0; top:125px; width:170px;"><div class="person-name">Daniel Hart</div><div class="person-role">Director</div></div>
  <ul class="contact" style="left:174px; top:125px;"><li><svg class="icon" viewBox="0 0 12 12"><rect x="2" y="4" width="8" height="6" rx="1" fill="#c82020"/><path d="M1 4q5-4 10 0" stroke="#c82020" stroke-width="2" fill="none"/></svg>t: +44 (0)1632 960415</li><li><svg class="icon" viewBox="0 0 12 12"><circle cx="6" cy="6" r="5" fill="#3d8fe0"/></svg>e: enquiries@runeestates.co.uk</li><li><svg class="icon" viewBox="0 0 12 12"><rect x="1" y="2" width="10" height="7" fill="#222"/><rect x="4" y="9" width="4" height="2" fill="#222"/></svg>w: runeestates.co.uk</li></ul>
</section>

<!-- Card 4 -->
<section class="card card-panel" style="left:469px; top:225px;">
  <div class="brand-box" style="left:12px; top:8px; width:118px; height:68px;"><span class="brand-mark"></span><span class="brand-name">RUNE</span></div>
  <ul class="address" style="left:12px; top:97px; width:118px; height:68px; background:var(--navy); color:var(--white); text-align:center; padding-top:4px; line-height:12px;"><li>RUNE Exclusive Estates</li><li>Elm Court House</li><li>Elm Court Lane</li><li>Amersham Vale</li><li>HP9 2QX</li></ul>
  <div style="left:148px; top:6px; width:185px; height:158px; border-radius:8px; border:2px solid #f0b84a; background:linear-gradient(180deg, #e8f1ff 0%, #9ec0ff 35%, var(--blue-card) 100%); box-shadow:0 6px 8px -4px rgba(0,0,0,.5);"></div>
  <div style="left:200px; top:0; width:70px; height:18px; background:var(--tag-yellow); border-radius:2px;"></div>
  <div class="person light" style="left:148px; top:40px; width:185px;"><div class="person-name">Daniel Hart</div><div class="person-role">Director</div></div>
  <ul class="contact" style="left:160px; top:105px; color:var(--white); line-height:16px;"><li>t: +44 (0)1632 960415</li><li>e: enquiries@runeestates.co.uk</li><li>w: runeestates.co.uk</li></ul>
</section>

<!-- Card 5 -->
<section class="card card-aqua" style="left:105px; top:416px;">
  <div role="img" aria-label="Illustration of city tower blocks" style="left:110px; top:80px; width:130px; height:99px; background:linear-gradient(180deg, rgba(255,255,255,0), rgba(255,255,255,.5));"></div>
  <div class="brand-box" style="left:20px; top:4px; width:115px; height:76px;"><span class="brand-mark"></span><span class="brand-name">RUNE</span></div>
  <div class="person light" style="left:140px; top:20px; width:200px;"><div class="person-name">Daniel Hart</div><div class="person-role">Director</div></div>
  <ul class="address right" style="left:0; top:88px; width:142px; color:var(--ink); line-height:16px;"><li>RUNE Exclusive Estates<span class="dot"></span></li><li>Elm Court House<span class="dot"></span></li><li>Elm Court Lane<span class="dot"></span></li><li>Amersham Vale<span class="dot"></span></li><li>HP9 2QX<span class="dot"></span></li></ul>
  <ul class="contact" style="left:170px; top:125px;"><li><span class="dot" style="border-radius:0;background:#333;"></span>t: +44 (0)1632 960415</li><li><span class="dot"></span>e: enquiries@runeestates.co.uk</li><li><span class="dot"></span>w: runeestates.co.uk</li></ul>
</section>

<!-- Card 6 -->
<section class="card card-mist" style="left:469px; top:416px;">
  <ul class="contact" style="left:6px; top:4px;"><li>t: +44 (0)1632 960415</li><li>e: enquiries@runeestates.co.uk</li><li>w: runeestates.co.uk</li></ul>
  <div role="img" aria-label="Green ribbon graphic" style="left:35px; top:88px; width:110px; height:40px; background:linear-gradient(90deg, var(--mint), #b8f5e6); transform:rotate(-8deg); opacity:.85;"></div>
  <div style="left:170px; top:0; width:116px; height:179px; background:var(--navy);"></div>
  <div class="brand-box" style="left:170px; top:4px; width:116px; height:60px;"><span class="brand-mark"></span><span class="brand-name">RUNE</span></div>
  <div role="img" aria-label="Purple ribbon bow" style="left:160px; top:72px; width:140px; height:45px; background:radial-gradient(ellipse at center, var(--violet) 0%, rgba(122,63,201,.3) 60%, rgba(122,63,201,0) 75%);"></div>
  <ul class="address right" style="left:0; top:88px; width:152px; color:var(--navy); line-height:16px;"><li>RUNE Exclusive Estates<span class="dot"></span></li><li>Elm Court House<span class="dot"></span></li><li>Elm Court Lane<span class="dot"></span></li><li>Amersham Vale<span class="dot"></span></li><li>HP9 2QX<span class="dot"></span></li></ul>
  <div class="person light" style="left:170px; top:132px; width:116px;"><div class="person-name" style="font-size:22px;">Daniel Hart</div><div class="person-role" style="font-size:12px;">Director</div></div>
</section>

<h2 class="section-label" style="left:105px; top:646px;">Letterhead</h2>
<section class="letterhead">
  <p class="address-line">RUNE Exclusive Estates<span class="bullet-sep">•</span>Elm Court House<span class="bullet-sep">•</span>Elm Court Lane<span class="bullet-sep">•</span>Amersham Vale<span class="bullet-sep">•</span>HP9 2QX</p>
  <div class="brand" style="display:flex; align-items:center; gap:8px;"><span class="brand-mark"></span><span class="brand-name" style="font-size:30px;">RUNE</span></div>
  <div class="sign-block"><p class="name">Daniel Hart</p><p class="lines">t: +44 (0)1632 960415<br>e: enquiries@runeestates.co.uk<br>w: runeestates.co.uk</p></div>
</section>

<h2 class="section-label" style="left:105px; top:810px;">Compliment Slip</h2>
<section class="slip">
  <header class="slip-header"><span class="brand-mark" style="margin-right:8px;"></span><span class="brand-name" style="font-size:30px;">RUNE</span></header>
  <div class="slip-rule"></div>
  <svg class="slip-curve" width="725" height="362" viewBox="0 0 725 362" aria-hidden="true">
    <path d="M500 362 C610 300 700 230 725 118 L725 362 Z" fill="var(--navy)"/>
  </svg>
  <div class="sign-block"><p class="name">Daniel Hart</p><p class="lines">t: +44 (0)1632 960415<br>e: enquiries@runeestates.co.uk<br>w: runeestates.co.uk</p></div>
  <footer class="slip-footer">RUNE Exclusive Estates<span class="bullet-sep">•</span>Elm Court House<span class="bullet-sep">•</span>Elm Court Lane<span class="bullet-sep">•</span>Amersham Vale<span class="bullet-sep">•</span>HP9 2QX</footer>
</section>

</body>
</html>
```